Jewelry Wholesale Business Card Design

Company name: VELORA
Business Background: Wholesale jewelry store located in downtown Los Angeles. We specialize in 18k gold-filled, stainless steel, 14kt gold, and natural stone jewelry.
website: www.velorashop.example
Instagram: velora_
Email: sales@velorashop.example
Address: 318 W. PRIOR ST #27, #109
LOS ANGELES, CA 90099
(213)555-0147

We would like to create a simple, yet elegant business card for my store
-Includes company logo
-Black background preferred
-Gold metallic color letters
- Lists the type of products we sell
-Small icons for instagram handle, phone, email, and website

Target Market(s)

Hispanic community, age 12-40

Industry/Entity Type

Jewelry Wholesale

Contact Information for Business Card

logo, business location, website, phone number, email, instagram, lists type of products, Dylan Morvet(my name)

Font styles to use
Serif
Sans Serif

Colors
FFF300
FFF600
FEFA6F
FFFEC7
FFFEE8

Requirements
Must have
• logo, business location, website, phone number, email, instagram, lists type of products, Dylan Morvet(my name)

```html
<!DOCTYPE html>
<html lang="en">
<head>
<meta charset="utf-8">
<title>VELORA Business Card</title>
<link rel="stylesheet" href="https://fonts.googleapis.com/css2?family=Marcellus&family=Arimo:wght@400&display=swap">
<style>
  :root {
    --backdrop: #2a2a2c;
    --card: #1b1c1e;
    --card-back: #0c0c0d;
    --gold: #f7c81a;
    --gold-light: #fef06f;
    --ink: #ffffff;
    --rule: #55575b;
    --glyph: #1b1c1e;
  }
  * { margin: 0; padding: 0; box-sizing: border-box; }
  html, body { width: 1200px; height: 1108px; overflow: hidden; background: var(--backdrop); }
  .stage {
    width: 1200px; height: 1108px;
    display: flex; justify-content: center; align-items: center; gap: 80px;
  }
  .card {
    width: 420px; height: 700px; border-radius: 28px; position: relative; overflow: hidden;
    box-shadow: 0 18px 40px rgba(0,0,0,.45);
  }
  .card-front { background: var(--card); text-align: center; color: var(--ink); }
  .brand-name {
    position: absolute; top: 170px; left: 0; right: 0;
    font-family: "Marcellus", serif; font-size: 86px; letter-spacing: 2px;
    color: var(--gold); line-height: 1;
  }
  .person-name {
    position: absolute; top: 378px; left: 0; right: 0;
    font-family: "Marcellus", serif; font-size: 34px; letter-spacing: 1px; color: var(--gold);
  }
  .icon-row {
    position: absolute; top: 432px; left: 40px; right: 40px;
    display: flex; align-items: center; justify-content: center; gap: 8px;
  }
  .icon-row .rule { flex: 1; height: 1px; background: var(--rule); }
  .icon {
    width: 38px; height: 38px; border-radius: 7px; background: var(--gold);
    display: flex; align-items: center; justify-content: center;
  }
  .icon svg { width: 24px; height: 24px; }
  .contact-list {
    position: absolute; top: 486px; left: 0; right: 0;
    font-family: "Arimo", sans-serif; font-size: 19px; line-height: 27px; list-style: none;
  }
  .divider {
    position: absolute; top: 605px; left: 70px; right: 70px; height: 1px; background: var(--rule);
  }
  .address {
    position: absolute; top: 620px; left: 0; right: 0;
    font-family: "Arimo", sans-serif; font-size: 19px; line-height: 27px; font-style: normal;
  }
  .card-back { background: var(--card-back); }
  .pattern-field {
    position: absolute; inset: 0;
    background: linear-gradient(215deg, #8d8e92 0%, #3a3b3e 28%, #141415 55%, #050505 100%);
  }
  .back-mark {
    position: absolute; top: 470px; left: 0; right: 0; text-align: center;
    font-family: "Marcellus", serif; font-size: 30px; color: var(--gold);
  }
  .product-list {
    position: absolute; bottom: 70px; left: 0; right: 0; text-align: center;
    font-family: "Arimo", sans-serif; font-size: 15px; line-height: 24px; color: var(--ink);
    letter-spacing: .3px;
  }
  .sep {
    display: inline-block; width: 7px; height: 7px; background: var(--gold);
    transform: rotate(45deg); margin: 0 7px 2px;
  }
</style>
</head>
<body>
<main class="stage">
  <section class="card card-front">
    <h1 class="brand-name">VELORA</h1>
    <h2 class="person-name">DYLAN MORVET</h2>
    <div class="icon-row">
      <span class="rule"></span>
      <span class="icon" aria-label="Phone">
        <svg viewBox="0 0 24 24"><path fill="var(--glyph)" d="M3 9c0-3 4-5 9-5s9 2 9 5v2h-5V9c-1-1-7-1-8 0v2H3zM6 13h12l2 7H4z"/><circle cx="12" cy="16.5" r="2" fill="var(--gold)"/></svg>
      </span>
      <span class="icon" aria-label="Email">
        <svg viewBox="0 0 24 24"><rect x="3" y="6" width="18" height="12" fill="var(--glyph)"/><path d="M3.5 6.5L12 13l8.5-6.5M3.5 17.5l6-5.5M20.5 17.5l-6-5.5" stroke="var(--gold)" stroke-width="1.3" fill="none"/></svg>
      </span>
      <span class="icon" aria-label="Website">
        <svg viewBox="0 0 24 24"><circle cx="12" cy="12" r="9" fill="var(--glyph)"/><path d="M3 12h18M12 3c-4 4-4 14 0 18M12 3c4 4 4 14 0 18" stroke="var(--gold)" stroke-width="1.2" fill="none"/></svg>
      </span>
      <span class="icon" aria-label="Social handle">
        <svg viewBox="0 0 24 24"><rect x="5" y="5" width="14" height="14" rx="2" fill="var(--glyph)"/></svg>
      </span>
      <span class="rule"></span>
    </div>
    <ul class="contact-list">
      <li>(213)555-0147</li>
      <li>sales@velorashop.example</li>
      <li>www.velorashop.example</li>
      <li>velora_</li>
    </ul>
    <div class="divider"></div>
    <address class="address">318 W. PRIOR ST #27, #109<br>LOS ANGELES, CA 90099</address>
  </section>

  <section class="card card-back">
    <div class="pattern-field" role="img" aria-label="Repeating glossy brand-mark pattern in black and silver tones"></div>
    <div class="back-mark">VELORA</div>
    <p class="product-list">
      18K GOLD-FILLED<span class="sep"></span>STAINLESS STEEL<span class="sep"></span>14KT GOLD<br>
      NATURAL STONE JEWELRY<span class="sep"></span>925 STERLING SILVER
    </p>
  </section>
</main>
</body>
</html>
```